120ml Jar Label — Masculine Cosmetic Foot Balm for Cracked, Hardworking Heels

We need a print-ready wraparound label for a 120ml jar — a brown/amber glass jar with a black metal screw lid (file photo attached).

--DO NOT PUT A BARCODE ON THE LABEL PLEASE--
**PLEASE READ "PLAN HUDDLE PROJECT BRIEF FINAL.MD" IN ATTACHED FILES IF YOU ARE SUBMITTING A DESIGN.**

The label is 190mm wide × 40mm high.
We need files to be in an .ai format with a 2mm bleed at the end.
Social media handle: @bramblekeepnz (facebook, instagram and tiktok)

Bramble Keep is a New Zealand foot-care brand making practical, no-nonsense products for hardworking men whose jobs wreck their feet. Our flagship product, Ridge Mender Balm, helps fix thick, cracked, hardworking skin.

Brand color scheme and overview is all in the brief file. You may add some brand aligned colors outside of the specified hex codes as you see fit to make a great design. Feel free to remove the "Bramble Keep" text from the logo so Bramble Keep is not doubled up on the front of the label

The tone we want: direct, rugged, and credible — like a workwear brand, not a spa brand. Most cracked-heel products on the market lean soft and feminine; we want to stand apart by looking like a serious fix for a real problem, made in New Zealand.

Full legal requirements for New Zealand cosmetic labelling (ingredients, directions, net contents, origin, etc.) are listed in the attached brief document — these are non-negotiable and must stay legible.

Please see the label attached "Label spacing guide" for this project's rough spacing guide. This label is the same size and sits well on the jar. This label doesn't need to be spaced quite as much as the Verin Label

I want to run the design for a week - I feel 7 days is a good amount of time for designers to see the work, digest the brief and create something remarkable and memorable for Bramble Keep.

Target Market(s)

Working men in New Zealand whose jobs or lifestyle put heavy wear on their feet — tradies, farmers, hospital/shift workers, hunters, and outdoors people. Practical, value-driven buyers rather than luxury skincare shoppers.

Industry/Entity Type

Beauty / Health & Wellness / Cosmetics

Font styles to use
Sans Serif
Other font styles liked:
• Montserrat (bold, headings), Inter (regular, body)

Colors
00AB8E
00BBA5
67D7C9
C6EFE9
E9F9F6
FFC000
F8CF3A
FAE287
FDF2CF
FEFAEE

Requirements
Must have
• All NZ cosmetic labelling requirements from the attached brief (product name, tag line, net contents, ingredients, directions, storage, made in NZ) — legible and complete, not omitted for aesthetics Fits 190mm × 40mm wraparound format for a 120ml brown jar with black lid Uses our existing brand colors: Deep Olive #3C4A34, Bone White #F4EFE6, Terracotta Clay #C1683D, and Warm Grey #4A4540 (exact palette in attached brief) Uses Montserrat (headings) and Inter (body) or close equivalents Incorporates our existing shield-and-wing logo (attached) Brand name and product name clearly readable from a normal shelf/bathroom-cabinet distance
Nice to have
• A style that could extend into a hero/product photo later, similar to the NZ-hills-backdrop look on our website (screenshot attached) — not required for the label itself, just good to keep in mind Original icon work (e.g. a small soak/apply/sock icon set) if it fits the rugged brand feel A design that could work as a small back-label/wraparound split if the front can't fit everything at a readable size
Should not have
• No pastel colors, floral motifs, or delicate script fonts — this should never look like spa/luxury skincare. Don't introduce new brand colors outside the palette provided other than black.

```html
<!DOCTYPE html>
<html lang="en">
<head>
<meta charset="utf-8">
<title>Bramble Keep — Ridge Mender Balm</title>
<link href="https://fonts.googleapis.com/css2?family=Montserrat:wght@500;600;700;800&family=Inter:wght@300;400;500&display=swap" rel="stylesheet">
<style>
  :root {
    --forest: #1f3a2e;
    --forest-deep: #1b3329;
    --clay: #b8703f;
    --bar-brown: #8b5a2b;
    --bone: #f2e8d8;
    --white: #ffffff;
    --ink-soft: #e9e4da;
    --page: #ffffff;
  }
  * { box-sizing: border-box; margin: 0; padding: 0; }
  html, body { width: 1196px; height: 1200px; overflow: hidden; background: var(--page); }
  body { position: relative; font-family: "Inter", sans-serif; }

  /* Website hero */
  .site { position: absolute; left: 253px; top: 102px; width: 705px; height: 401px; overflow: hidden; }
  .announce { height: 26px; background: var(--bar-brown); display: flex; align-items: center; position: relative; }
  .announce .socials { position: absolute; left: 100px; display: flex; gap: 8px; }
  .announce .socials span { width: 6px; height: 6px; border-radius: 50%; background: var(--forest); }
  .announce p { margin: 0 auto; width: 190px; text-align: center; font: 700 6px/1.2 "Montserrat", sans-serif; color: var(--forest); }
  .nav { height: 38px; background: var(--forest); display: flex; align-items: center; padding-left: 100px; position: relative; }
  .nav .brand { font: 700 6px/1 "Montserrat", sans-serif; color: var(--bone); width: 40px; text-align: center; }
  .nav ul { list-style: none; display: flex; gap: 12px; margin-left: 10px; }
  .nav li { font: 400 6.5px/1 "Inter", sans-serif; color: var(--ink-soft); }
  .nav li.current { text-decoration: underline; }
  .nav .tools { position: absolute; right: 112px; display: flex; gap: 9px; }
  .hero { position: relative; height: 337px; border-top: 4px solid #2b2b2b; }
  .hero-photo { position: absolute; inset: 0; background: linear-gradient(180deg, #c9b697 0%, #a98e62 30%, #7c6a43 55%, #4e4a2d 80%, #3a3624 100%); }
  .hero h1 { position: absolute; left: 41px; top: 100px; width: 300px; font: 500 21.5px/1.22 "Montserrat", sans-serif; color: var(--white); }
  .hero .cta { position: absolute; left: 43px; top: 218px; width: 75px; height: 40px; border: 1.5px solid var(--white); border-radius: 20px; font: 500 9.5px/37px "Montserrat", sans-serif; color: var(--white); text-align: center; }

  /* Logo card */
  .logo-card { position: absolute; left: 614px; top: 531px; width: 337px; height: 202px; background: var(--forest); display: flex; flex-direction: column; align-items: center; justify-content: center; gap: 12px; }
  .logo-card .mark { width: 64px; height: 64px; border-radius: 50%; background: var(--clay); }
  .logo-card .name { font: 800 26px/1 "Montserrat", sans-serif; color: var(--bone); text-align: center; }
  .logo-card .name small { display: block; font-size: 14px; margin-top: 4px; }

  /* Jar label, flat */
  .label { position: absolute; left: 207px; top: 872px; width: 809px; height: 184px; background: var(--forest-deep); color: var(--white); }
  .label .heading { color: var(--clay); font-weight: 500; }
  .label .directions { position: absolute; left: 28px; top: 35px; width: 275px; font: 400 11.5px/1.25 "Inter", sans-serif; text-align: justify; }
  .label .storage { position: absolute; left: 27px; top: 131px; width: 240px; font: 400 11.5px/1.25 "Inter", sans-serif; }
  .label .front { position: absolute; left: 412px; top: 25px; width: 220px; height: 150px; }
  .label .brand-name { font: 700 27px/1.18 "Montserrat", sans-serif; color: var(--white); }
  .label .front-mark { position: absolute; left: 130px; top: 4px; display: flex; flex-direction: column; align-items: center; gap: 5px; }
  .label .front-mark span { width: 34px; height: 34px; border-radius: 50%; background: var(--clay); }
  .label .front-mark b { font: 800 9px/1.1 "Montserrat", sans-serif; color: var(--bone); text-align: center; }
  .label .product { margin-top: 8px; font: 300 18.5px/1 "Inter", sans-serif; color: var(--clay); }
  .label .tagline { margin-top: 6px; font: 400 10.5px/1 "Inter", sans-serif; letter-spacing: .6px; }
  .label .meta { position: absolute; left: 0; top: 131px; width: 220px; display: flex; justify-content: space-between; font: 400 12px/1 "Inter", sans-serif; }
  .label .meta .volume { letter-spacing: .5px; }
  .label .ingredients { position: absolute; left: 637px; top: 42px; width: 162px; font: 400 10.2px/1.18 "Inter", sans-serif; }
</style>
</head>
<body>

<section class="site">
  <div class="announce">
    <div class="socials"><span></span><span></span><span></span></div>
    <p>Flat Rate $10 Shipping On all order below $80</p>
  </div>
  <nav class="nav">
    <div class="brand">BRAMBLE KEEP</div>
    <ul>
      <li class="current">Home</li><li>Products</li><li>About Us</li><li>Guides</li><li>FAQ</li><li>Contact</li>
    </ul>
    <div class="tools">
      <svg width="9" height="9" viewBox="0 0 10 10" fill="none" stroke="#e9e4da" stroke-width="1"><circle cx="4" cy="4" r="3"/><path d="M6.3 6.3 9 9"/></svg>
      <svg width="9" height="9" viewBox="0 0 10 10" fill="none" stroke="#e9e4da" stroke-width="1"><circle cx="5" cy="3" r="2"/><path d="M1 9.5c0-2.5 8-2.5 8 0Z"/></svg>
      <svg width="9" height="9" viewBox="0 0 10 10" fill="none" stroke="#e9e4da" stroke-width="1"><path d="M1.5 3h7l-.7 6H2.2Z"/><path d="M3.5 3a1.5 1.5 0 0 1 3 0"/></svg>
    </div>
  </nav>
  <div class="hero">
    <div class="hero-photo" role="img" aria-label="Golden hour New Zealand hills with tussock grass and a balm jar resting on a tree stump"></div>
    <h1>Cracked heels from long Days on the tools? Here’s The fix that works</h1>
    <div class="cta">SHOP ALL</div>
  </div>
</section>

<section class="logo-card">
  <div class="mark"></div>
  <div class="name">BRAMBLE KEEP<small>NZ</small></div>
</section>

<section class="label">
  <div class="directions">
    <span class="heading">Directions:</span><br>
    Apply generously to clean, dry feet, focusing on heels and thick or cracked areas. For cracked heels, wear our moisture-locking socks overnight. Use daily.
  </div>
  <div class="storage">
    <span class="heading">Storage:</span> keep out of direct sunlight. Best used within six months of opening.
  </div>
  <div class="front">
    <div class="brand-name">Bramble<br>Keep</div>
    <div class="front-mark"><span></span><b>BRAMBLE KEEP<br>NZ</b></div>
    <div class="product">Ridge Mender Balm</div>
    <div class="tagline">For Hardworking Soles</div>
    <div class="meta"><span class="volume">120ml</span><span>Made in New Zealand</span></div>
  </div>
  <div class="ingredients">
    <span class="heading">Ingredients:</span> Shea Butter, Beef Tallow, Beeswax, Grape Seed Oil, Vegetable Glycerin, Lanolin, Propylene Glycol, Panthenol, Gluconolactone &amp; Sodium Benzoate, Manuka Honey, Allantoin, Vitamin E, Tea Tree Essential Oil, Lemon Myrtle Essential Oil, Rosemary Oleoresin Extract
  </div>
</section>

</body>
</html>
```